New Professional Business Web Site

We need a web design for an existing company based in Dallas called "FoxTrail".
We provide software and professional services to enterprise customers in the contact centre space. We have a global customer base but primarily US and UK.
Our initial products are as follows-
LineSight - an application that helps Vortiva contact centre managers and administrators observe individual calls in queue.
MassLoad - an application that allows Vortiva administrators to load large groups of extensions and associate them to places.
Clustra - an application that helps Vortiva customers manage multilayers of agent and place groups into hiearchical and geographical groups of groups.
We would like to see designs that use the colors black, gray, and red as this matches with our new logo we have had designed from this web site and will have available in a few days.
The final design should communicate professionalism, innovation, software, large corporation, and telecommunications.
We're looking to provide features like-
1) Interactive Support Portal for customers
2) Product Descriptions
3) Product Purchasing
4) Interactive Forum
Target Market(s)
enterprise companies interested in call center related products and services
Industry/Entity Type
Business

```html
<!DOCTYPE html>
<html lang="en">
<head>
<meta charset="utf-8">
<title>FoxTrail — Software and Services</title>
<link rel="stylesheet" href="https://fonts.googleapis.com/css2?family=Aldrich&family=Open+Sans:wght@400;700&family=Arimo:wght@400;700&display=swap">
<style>
  :root {
    --page: #0d0d0d;
    --red: #c70000;
    --white: #ffffff;
    --muted: #9a9a9a;
    --line: #3a3a3a;
  }
  * { box-sizing: border-box; margin: 0; padding: 0; }
  html, body { width: 1200px; height: 994px; overflow: hidden; background: var(--page); }
  body { position: relative; font-family: "Arimo", Arial, sans-serif; color: var(--white); }

  .site { position: absolute; left: 24px; top: 0; width: 1153px; height: 994px; background: #000; }

  /* header */
  .header { position: absolute; left: 0; top: 0; width: 1153px; height: 131px;
    background: radial-gradient(ellipse 180px 140px at 170px 40px, #4a4a4a 0%, #1a1a1a 60%, #0e0e0e 100%); }
  .brand { position: absolute; left: 30px; top: 52px; display: flex; align-items: center; gap: 12px; }
  .brand-dot { width: 30px; height: 30px; border-radius: 50%; background: var(--red); }
  .brand-name { font-family: "Open Sans", sans-serif; font-weight: 700; font-size: 40px; color: #cfcfcf; }
  .contact-bar { position: absolute; left: 685px; top: 27px; display: flex; align-items: center; font-size: 15px; }
  .contact-bar .hello { color: var(--white); }
  .contact-bar .phone { color: var(--muted); margin-left: 18px; }
  .contact-bar .touch { color: var(--white); margin-left: 56px; }
  .social { display: flex; gap: 12px; margin-left: 24px; }
  .social span { width: 24px; height: 24px; border-radius: 50%; background: #6e6e6e; display: block; }
  .main-nav { position: absolute; right: 32px; top: 86px; display: flex; gap: 31px; font-size: 14px; text-transform: uppercase; }
  .main-nav a, .foot-nav a { color: var(--white); text-decoration: none; }

  /* hero */
  .hero { position: absolute; left: 0; top: 131px; width: 1153px; height: 338px;
    background: radial-gradient(ellipse 260px 220px at 260px 170px, #e50000 0%, transparent 100%),
                linear-gradient(180deg, #bf0000 0%, #c40000 65%, #8a0000 100%); }
  .hero-devices { position: absolute; left: 36px; top: 40px; width: 368px; height: 275px;
    border-radius: 18px; background: linear-gradient(160deg, #2b2b2b 0%, #111 40%, #dcdcdc 41%, #f4f4f4 100%); }
  .hero-title { position: absolute; left: 560px; top: 66px; font-family: "Aldrich", sans-serif; font-size: 45px; font-weight: 400; }
  .hero-text { position: absolute; left: 560px; top: 149px; width: 345px; font-size: 19px; line-height: 24px; }
  .btn { position: absolute; left: 561px; top: 272px; width: 200px; height: 46px;
    background: linear-gradient(180deg, #4a4a4a 0%, #111 55%, #000 100%);
    font-size: 23px; line-height: 46px; text-align: center; color: var(--white); text-decoration: none; }

  /* features */
  .content { position: absolute; left: 0; top: 469px; width: 1153px; height: 431px;
    background: radial-gradient(ellipse 500px 300px at 700px 100px, #2c2c2c 0%, #121212 70%); }
  .features { position: absolute; left: 0; top: 0; width: 387px; height: 431px; border-right: 2px solid var(--line); }
  .feature { position: absolute; left: 0; width: 385px; height: 90px; }
  .feature-icon { position: absolute; left: 22px; top: 0; width: 82px; height: 82px; border-radius: 8px;
    background: linear-gradient(160deg, #d8d8d8, #6e6e6e); }
  .feature-title { position: absolute; left: 154px; top: 6px; font-family: "Open Sans", sans-serif; font-weight: 700; font-size: 20px; line-height: 24px; white-space: nowrap; }
  .feature-text { position: absolute; left: 154px; top: 32px; width: 205px; font-family: "Open Sans", sans-serif; font-size: 14.5px; line-height: 19px; color: var(--muted); }
  .more { position: absolute; left: 154px; top: 72px; width: 40px; height: 13px; font-size: 10px; line-height: 13px;
    background: #5a5a5a; color: var(--white); padding-left: 13px; }
  .more::before { content: ""; position: absolute; left: 0; top: 0; width: 11px; height: 13px; background: var(--red); }

  .services { position: absolute; left: 419px; top: 40px; width: 706px; }
  .section-title { font-size: 35px; font-weight: 400; line-height: 40px; }
  .services p { margin-top: 8px; font-size: 15px; line-height: 21px; text-align: justify; }
  .products-title { margin-top: 10px; }
  .products { margin-top: 2px; display: flex; gap: 21px; }
  .product { width: 160px; text-align: center; }
  .product-shot { height: 160px; border: 1px solid #333; background: #000; padding: 18px 6px; }
  .product-shot div { width: 100%; height: 100%; background: linear-gradient(180deg, #e8e8e8, #bfc8d8); }
  .product-shot.network div { background: linear-gradient(160deg, #3f6fc9 0%, #1d3f8a 60%, #0c1c44 100%); }
  .product-name { margin-top: 6px; font-size: 17px; }
  .product-name.strong { font-family: "Open Sans", sans-serif; font-weight: 700; }

  /* footer */
  .footer { position: absolute; left: 4px; top: 907px; width: 1142px; height: 87px; border-radius: 6px 6px 0 0;
    background: linear-gradient(180deg, #3a3a3a 0%, #1e1e1e 100%); }
  .foot-nav { position: absolute; left: 20px; top: 22px; display: flex; gap: 31px; font-size: 14px; text-transform: uppercase; }
  .copyright { position: absolute; left: 21px; top: 55px; font-family: "Open Sans", sans-serif; font-size: 13px; color: var(--muted); }
  .copyright b { color: var(--white); font-weight: 400; }
  .foot-contact { position: absolute; right: 22px; top: 50px; display: flex; align-items: center; font-size: 15px; }
  .foot-contact .social { margin-left: 22px; }
</style>
</head>
<body>
<div class="site">
  <header class="header">
    <div class="brand"><span class="brand-dot"></span><span class="brand-name">FoxTrail</span></div>
    <div class="contact-bar">
      <span class="hello">Say Hello</span><span class="phone">+1 555 0142 880</span>
      <span class="touch">Get intouch</span>
      <div class="social"><span></span><span></span><span></span></div>
    </div>
    <nav class="main-nav">
      <a href="#">Home</a><a href="#">What we do</a><a href="#">About us</a><a href="#">Products</a>
      <a href="#">Services</a><a href="#">Benefits</a><a href="#">Contact us</a>
    </nav>
  </header>

  <section class="hero">
    <div class="hero-devices" role="img" aria-label="Tablet and phone showing the app dashboard"></div>
    <h1 class="hero-title">Connecting Everyone</h1>
    <p class="hero-text">Lorem Ipsum is simply dummy text of the printing and typesetting industry.Lorem Ipsum is simply dummy text of the printing and typesetting .</p>
    <a class="btn" href="#">Learn More</a>
  </section>

  <main class="content">
    <aside class="features">
      <div class="feature" style="top:52px">
        <div class="feature-icon" role="img" aria-label="Film strip and popcorn icon"></div>
        <h3 class="feature-title">Product Descriptions</h3>
        <p class="feature-text">See the app live in action on some of the latest phones.</p>
        <span class="more">More</span>
      </div>
      <div class="feature" style="top:185px">
        <div class="feature-icon" role="img" aria-label="Two users icon"></div>
        <h3 class="feature-title">Interactive Forum</h3>
        <p class="feature-text">Try before you buy. Download the latest free trial version.</p>
        <span class="more">More</span>
      </div>
      <div class="feature" style="top:324px">
        <div class="feature-icon" role="img" aria-label="Support agent with headset icon"></div>
        <h3 class="feature-title">Interactive Support</h3>
        <p class="feature-text">Need help? found a bug? we can help. Free Tech Support.</p>
        <span class="more">More</span>
      </div>
    </aside>

    <section class="services">
      <h2 class="section-title">Our Software and Services</h2>
      <p>Lorem ipsum dolor sit amet, consectetur adipiscing elit. Aliquam eu ornare enim. Vestibulum ut arcu ipsum, nec semper eros. Nam accumsan placerat consectetur. Aliquam erat volutpat. Nullam nec justo justo. Maecenas aliquam mollis erat in rhoncus. Mauris metus sem, lobortis et rutrum feugiat, pharetra id risus.</p>
      <h2 class="section-title products-title">Products</h2>
      <div class="products">
        <div class="product"><div class="product-shot"><div role="img" aria-label="MassLoad screenshot"></div></div><div class="product-name">MassLoad</div></div>
        <div class="product"><div class="product-shot"><div role="img" aria-label="LineSight screenshot"></div></div><div class="product-name">LineSight</div></div>
        <div class="product"><div class="product-shot"><div role="img" aria-label="Clustra screenshot"></div></div><div class="product-name">Clustra</div></div>
        <div class="product"><div class="product-shot network"><div role="img" aria-label="Illustration of a globe with a network cable"></div></div><div class="product-name strong">More to come</div></div>
      </div>
    </section>
  </main>

  <footer class="footer">
    <nav class="foot-nav">
      <a href="#">Home</a><a href="#">What we do</a><a href="#">About us</a><a href="#">Products</a>
      <a href="#">Services</a><a href="#">Benefits</a><a href="#">Contact us</a>
    </nav>
    <p class="copyright">Copyright <b>FOXTRAIL</b>, All Rights Reserved</p>
    <div class="foot-contact"><span>Get intouch</span><div class="social"><span></span><span></span><span></span></div></div>
  </footer>
</div>
</body>
</html>
```